Merrowind Flyer

A simple flyer that gets people attention
I have a attached a sample of what we use now and a picture we use
We service gas fireplaces and need a eye catching but not to cluttered flyer to promote our business. the cost per fireplace should be $60.00

Reason: Sorry for the delay We are out of town on holidays with sketchy internet service To frustrating to complete this project till I am back in a week Thank you for your patience Kind regards Dale

```html
<!DOCTYPE html>
<html lang="en">
<head>
<meta charset="utf-8">
<title>Merrowind Gas Services – Fireplace Service Notice</title>
<link href="https://fonts.googleapis.com/css2?family=Lato:wght@300;400;700;900&family=Fjalla+One&display=swap" rel="stylesheet">
<style>
  :root {
    --orange: #e0752c;
    --orange-deep: #c8571c;
    --brown: #8a3f16;
    --yellow: #ecd431;
    --gold: #ffd21f;
    --red-burst: #e0401c;
    --ink: #2b2b2b;
    --grey-ink: #4a4a4a;
    --white: #ffffff;
  }
  * { margin: 0; padding: 0; box-sizing: border-box; }
  html, body { width: 1004px; height: 1200px; overflow: hidden; background: #f2f2f2; }
  .flyer {
    position: relative; width: 1004px; height: 1200px; overflow: hidden;
    background: var(--yellow);
    font-family: "Lato", Arial, sans-serif;
  }
  .hero-photo {
    position: absolute; left: 0; top: 0; width: 1004px; height: 560px;
    background:
      radial-gradient(ellipse at 55% 25%, #f39a2a 0%, #b5531a 22%, rgba(60,25,10,0) 50%),
      linear-gradient(180deg, #3b2015 0%, #5a3020 45%, #c98a6a 75%, #7a5040 100%);
  }
  .hero-title { position: absolute; top: 14px; width: 100%; text-align: center; }
  .hero-title .notice {
    color: var(--white); font-weight: 900; font-size: 40px; letter-spacing: 0.5px; line-height: 1.1;
  }
  .hero-title .property {
    color: var(--gold); font-weight: 300; font-size: 46px; letter-spacing: 1px; line-height: 1.15;
  }
  .price-ribbon { position: absolute; left: 0; top: 410px; width: 1004px; height: 240px; }
  .price-ribbon svg { position: absolute; inset: 0; }
  .price-ribbon .ribbon-text {
    position: absolute; left: 60px; top: 100px; width: 900px; line-height: 50px;
    transform: rotate(-4.6deg); transform-origin: left center;
    color: var(--white); font-weight: 900; font-size: 31px; white-space: nowrap;
  }
  .ribbon-text .amount {
    font-family: "Fjalla One", "Arial Narrow", sans-serif; font-weight: 400;
    color: var(--gold); font-size: 50px; vertical-align: -4px; margin-left: 6px;
  }
  .service-copy {
    position: absolute; left: 40px; top: 640px; width: 930px;
    color: var(--ink); font-size: 13.2px; line-height: 1.32; text-align: justify;
  }
  .service-copy p + p { margin-top: 13px; }
  .lower-panel { position: absolute; left: 0; top: 0; width: 1004px; height: 1200px; }
  .lower-panel svg { position: absolute; inset: 0; }
  .signs-box {
    position: absolute; left: 0; top: 915px; width: 546px; height: 234px;
    background: linear-gradient(180deg, var(--orange) 0%, var(--orange-deep) 100%);
    border-radius: 0 16px 16px 0;
    padding: 20px 24px 0 26px;
  }
  .signs-box h2 {
    font-family: "Fjalla One", "Arial Narrow", sans-serif; font-weight: 400;
    color: var(--gold); font-size: 29px; line-height: 1.3; letter-spacing: 0.5px;
  }
  .signs-box p { margin-top: 16px; color: var(--white); font-size: 17px; line-height: 1.35; }
  .contact { position: absolute; left: 554px; top: 1044px; }
  .contact .label {
    font-family: "Fjalla One", "Arial Narrow", sans-serif; color: var(--grey-ink);
    font-size: 19px; line-height: 1.25; letter-spacing: 0.5px;
  }
  .contact .company { color: var(--orange-deep); font-size: 19px; margin-top: 2px; }
  .contact .phone { color: var(--grey-ink); font-size: 19px; display: flex; align-items: center; gap: 6px; }
  .contact .phone svg { width: 14px; height: 14px; }
  .price-burst { position: absolute; left: 752px; top: 826px; width: 230px; height: 230px; }
  .price-burst .ray {
    position: absolute; left: 33px; top: 33px; width: 164px; height: 164px;
    background: var(--red-burst);
  }
  .price-burst .ray:nth-child(2) { transform: rotate(22.5deg); }
  .price-burst .ray:nth-child(3) { transform: rotate(45deg); }
  .price-burst .ray:nth-child(4) { transform: rotate(67.5deg); }
  .price-burst .burst-text {
    position: absolute; left: 35px; top: 50px; width: 160px; text-align: center;
    color: var(--white); font-size: 13.5px; line-height: 1.28;
  }
  .burst-text .headline {
    font-family: "Fjalla One", "Arial Narrow", sans-serif; color: var(--gold);
    font-size: 20px; display: block; line-height: 1.2; white-space: nowrap;
  }
  .brand-mark {
    position: absolute; left: 852px; top: 1100px;
    display: flex; align-items: center; gap: 6px;
    color: var(--orange-deep); font-weight: 900; font-size: 20px;
  }
  .brand-mark .dot { width: 12px; height: 12px; background: var(--orange-deep); }
  .bottom-band { position: absolute; left: 0; top: 1176px; width: 1004px; height: 24px; background: var(--yellow); }
</style>
</head>
<body>
<div class="flyer">
  <div class="hero-photo" role="img" aria-label="Photo: a family's bare feet warming in front of a lit gas fireplace"></div>
  <div class="hero-title">
    <div class="notice">NOTICE TO THE OWNERS</div>
    <div class="property">NAME OF PROPERTY</div>
  </div>

  <div class="lower-panel">
    <svg viewBox="0 0 1004 1200" width="1004" height="1200" aria-hidden="true">
      <defs>
        <linearGradient id="panelGrey" x1="0" y1="0" x2="0" y2="1">
          <stop offset="0" stop-color="#ffffff"/>
          <stop offset="1" stop-color="#d9d9d9"/>
        </linearGradient>
      </defs>
      <polygon points="0,868 485,905 1004,842 1004,1176 0,1176" fill="url(#panelGrey)"/>
      <polyline points="0,866 485,903 1004,840" fill="none" stroke="#e0752c" stroke-width="3"/>
    </svg>
  </div>
  <div class="lower-panel" role="img" aria-label="Faint photo of warm hands and feet by the fire behind the lower panel" style="top:880px;height:296px;background:linear-gradient(180deg,rgba(255,255,255,0) 0%,rgba(200,200,200,0.25) 100%);"></div>

  <div class="price-ribbon">
    <svg viewBox="0 0 1004 240" width="1004" height="240" aria-hidden="true">
      <polygon points="0,190 27,190 27,221" fill="#8a3f16"/>
      <polygon points="962,20 1004,16 1004,104 962,114" fill="#8a3f16"/>
      <polygon points="0,96 962,20 962,114 0,190" fill="#e0752c"/>
      <polygon points="0,96 962,20 962,30 0,106" fill="#ec8a3e"/>
    </svg>
    <div class="ribbon-text">THE COST PER FIREPLACE SHOULD BE <span class="amount">$60.00</span></div>
  </div>

  <div class="service-copy">
    <p>MERROWIND GAS SERVICES will be on site conducting gas fireplace safety inspections and maintenance for <strong>NAME OF PROPERTY</strong> on <strong>DATE OF SERVICE.</strong> If you wish to have your fireplace serviced, please put your name and unit number on the sign-up sheet provided. We will require approximately 20 - 30 minutes to service each fireplace and require that the fireplace is cool to conduct the work. <strong>Please do not use your fireplace within 2 hours of your appointment as we do not want the technicians to receive burns.</strong></p>
    <p>The Northfield Home Energy Office states that all fireplaces require regular servicing. Fireplace manufacturers recommend each unit be serviced annually by a qualified technician and insurance companies and Fire Departments are now asking for reports regarding fireplace safety inspections and servicing. The service Merrowind Gas Services will provide will entail a thorough assessment of pilot, burner and valve operation, a door seal inspection, an inspection of the electrical circuits, repositioning of the logs, cleaning and adjustment of fan and controls, cleaning of the firebox and glass, a carbon monoxide test, testing of fittings for gas leaks and a complete operational test once the service is complete.</p>
  </div>

  <div class="signs-box">
    <h2>POSSIBLE INDICATION THAT YOUR GAS<br>FIREPLACE REQUIRES SERVICE INCLUDE:</h2>
    <p><strong>(1)</strong> Cloudy film on glass, <strong>(2)</strong> Strong odors when fireplace is in operation, <strong>(3)</strong> Soot build up on glass, logs or exterior of building, <strong>(4)</strong> Tarnished/discolored brass, <strong>(5)</strong> Pilot light outages, <strong>(6)</strong> Main burner is not lighting consistently. <strong>(7)</strong></p>
  </div>

  <div class="contact">
    <div class="label">FOR FURTHER INFORMATION<br>PLEASE CONTACT MAREN AT:</div>
    <div class="company">Merrowind Gas Services</div>
    <div class="phone">
      <svg viewBox="0 0 16 16" aria-hidden="true"><rect width="16" height="16" rx="3" fill="#c8571c"/><path d="M5 3.5c.6 0 1 .9 1.3 1.7.2.5-.4 1-.6 1.3.5 1.2 1.4 2.1 2.6 2.6.3-.3.8-.9 1.3-.6.8.4 1.7.7 1.7 1.3 0 .9-.9 1.7-1.8 1.7C6.3 11.5 4.5 8.9 3.4 6.2 3.1 5.1 4 3.5 5 3.5z" fill="#fff"/></svg>
      604.555.0187
    </div>
  </div>

  <div class="price-burst">
    <div class="ray"></div><div class="ray"></div><div class="ray"></div><div class="ray"></div>
    <div class="burst-text">
      <span class="headline">THE COST IS $55.00</span>
      (tax included)<br>(Owners must have payment ready at time of inspection. Payment may be made in the form of cash, cheque or credit card)
    </div>
  </div>

  <div class="brand-mark"><span class="dot"></span>Merrowind</div>

  <div class="bottom-band"></div>
</div>
</body>
</html>
```